Create Lanternfield HR Business Cards.

Create Business Cards for Lanternfield HR. 2 sided and Would like the back to have the logo.

Info for Business Card:
Address: 4827 Millbrook Ave Suite 230 Cleveland, Ohio 44987
Office Number: 216-555-0143
Mobile: 216-555-0192

Website: www.lanternfieldhr.example

Target Market(s)

Small to medium size businesses

Industry/Entity Type

Human Resources

Contact Information for Business Card

Company logo and information

Font styles to use
Serif
Sans Serif

Requirements
Must have
• Info for Business Card: Address: 4827 Millbrook Ave Suite 230 Cleveland, Ohio 44987 Office Number: 216-555-0143 Mobile: 216-555-0192 Website: www.lanternfieldhr.example

```html
<!DOCTYPE html>
<html lang="en">
<head>
<meta charset="utf-8">
<title>Lanternfield HR Business Card</title>
<link rel="stylesheet" href="https://fonts.googleapis.com/css2?family=Red+Hat+Display:wght@500;700;800&display=swap">
<style>
  :root {
    --teal: #076878;
    --orange: #f0872a;
    --plum: #3c2148;
    --white: #ffffff;
    --text-font: "Red Hat Display", sans-serif;
  }
  * { margin: 0; padding: 0; box-sizing: border-box; }
  html, body { width: 1200px; height: 1199px; overflow: hidden; background: var(--teal); }
  .card-sheet { position: relative; width: 1200px; height: 1199px; font-family: var(--text-font); color: var(--white); }
  .card-side { position: absolute; left: 0; width: 1200px; overflow: hidden; background: var(--teal); }
  .card-front { top: 0; height: 600px; }
  .card-back { top: 600px; height: 599px; }
  .stripes { position: absolute; inset: 0; width: 100%; height: 100%; }

  .brand-disc {
    position: absolute; left: 310px; top: 10px; width: 580px; height: 580px;
    border-radius: 50%; background: var(--white);
    display: flex; align-items: center; justify-content: center; text-align: center;
  }
  .brand-disc__name {
    font-weight: 800; font-size: 66px; line-height: 1.05; color: var(--plum);
  }

  .header-mark {
    position: absolute; left: 81px; top: 31px; width: 128px; height: 128px;
    border-radius: 50%; background: var(--white);
  }
  .header-name {
    position: absolute; left: 336px; top: 52px; white-space: nowrap;
    font-weight: 500; font-size: 70px; letter-spacing: 6px; line-height: 1; color: var(--white);
  }
  .header-rule { position: absolute; left: 0; top: 176px; width: 1200px; height: 3px; background: var(--white); }

  .contact { position: absolute; left: 32px; font-weight: 700; white-space: nowrap; line-height: 1; }
  .contact--heading { top: 262px; left: 34px; font-size: 80px; }
  .contact--address { top: 355px; font-size: 39px; letter-spacing: -0.3px; }
  .contact--office { top: 408px; font-size: 40px; }
  .contact--mobile { top: 462px; font-size: 40px; }
  .contact--web { top: 537px; left: 0; width: 1200px; text-align: center; font-size: 40px; }
</style>
</head>
<body>
<main class="card-sheet">
  <section class="card-side card-front" aria-label="Card front">
    <svg class="stripes" viewBox="0 0 1200 600" aria-hidden="true">
      <!-- bands follow lines y = c - 0.577x -->
      <polygon fill="var(--orange)" points="0,447 775,0 962,0 0,555"/>
      <polygon fill="var(--plum)" points="0,555 962,0 1213,0 0,700"/>
      <polygon fill="var(--orange)" points="0,700 1213,0 1200,0 1200,140 0,832"/>
    </svg>
    <div class="brand-disc">
      <p class="brand-disc__name">Lanternfield<br>HR</p>
    </div>
  </section>

  <section class="card-side card-back" aria-label="Card back">
    <svg class="stripes" viewBox="0 0 1200 599" aria-hidden="true">
      <polygon fill="var(--orange)" points="0,516 894,0 1109,0 0,640"/>
      <polygon fill="var(--plum)" points="0,640 1109,0 1200,0 1200,68 0,760"/>
      <polygon fill="var(--orange)" points="0,760 1200,68 1200,202 0,894"/>
    </svg>
    <div class="header-mark"></div>
    <h1 class="header-name">LANTERNFIELD HR</h1>
    <div class="header-rule"></div>

    <p class="contact contact--heading">Address&nbsp;&nbsp;:</p>
    <p class="contact contact--address">4827 Millbrook Ave Suite 230 Cleveland, Ohio 44987</p>
    <p class="contact contact--office">Office Number: 216-555-0143</p>
    <p class="contact contact--mobile">Mobile: 216-555-0192</p>
    <p class="contact contact--web">Website: Www.lanternfieldhr.example</p>
  </section>
</main>
</body>
</html>
```